Design for the A4 Letterhead, envelope and A4 Folder

Design have to be clean, professional, unique (eye catchy) and high end.
Colors: Yellow (Code: 803C), Darker Grey and Black or white (optional)
Logo can be in white or black

Letterhead:
Contain: 1. Korvanel Logo
2. Slogan "MADE WITH PRIDE"
3. Company information:
Korvanel Valves Pte. Ltd. (Singapore)
Registration no: 201947162K
Tel: (65) 6218 4906
Fax: (65) 6241 7089
Email: sales@korvanelvalves.example
Website: http://www.korvanelvalves.example
4. Logo watermark

Envelope:
Contain: 1. Korvanel Logo
3. website: http://www.korvanelvalves.example and email address:
sales@korvanelvalves.example
4. Logo watermark

Folder:
Contain: 1. Korvanel Logo
3. Company's information:
Tel: (65) 6218 4906
Fax: (65) 6241 7089
4. QR Code
5. Logo watermark
6. On the inside there is a space to insert business card. Contrast colors
between the inside and cover.

For the Folder design, please be informed that we would prefer to have the Korvanel logo on the left hand side of the cover page, rather than on the right hand side.And also if we could highlight the "Made with Pride" slogan with either the yellow box or black/grey box depending on the background color.For the Envelope design,it does not matter where the position of the logo is. But please also highlight the "Made with Pride" Slogan For the Letterhead design, the position of the logo must be on the left hand side and the slogan must be highlighted. In addition, please include the following company information (only for the letterhead design)Korvanel Valves Pte. Ltd. (Singapore)Registration no: 201947162KTel: (65) 6218 4906Fax: (65) 6241 7089Email: sales@korvanelvalves.exampleWebsite: http://www.korvanelvalves.example Added Wednesday, August 2, 2017

Target Market(s)

Business to Business, High End market

Industry/Entity Type

It Professional

Font styles to use
Serif

Requirements
Must have
• Design have to be clean, professional, unique (eye catchy) and high end.
Nice to have
• color contrast but still maintaining the professionalism and the seriousness
Should not have
• Messy look, futuristic look, too crowded

```html
<!DOCTYPE html>
<html lang="en">
<head>
<meta charset="utf-8">
<title>Korvanel Valves – Stationery</title>
<link href="https://fonts.googleapis.com/css2?family=Source+Sans+3:wght@400;600&display=swap" rel="stylesheet">
<style>
  :root {
    --yellow: #fcec22;
    --ink: #555555;
    --ink-dark: #3a3a3a;
    --paper: #f5f4f2;
    --band-grey: #4a4a4a;
    --mark-faint: #e9e8e6;
    --bg-top: #8c8c8c;
    --bg-bottom: #585858;
  }
  * { margin: 0; padding: 0; box-sizing: border-box; }
  html, body { width: 1200px; height: 754px; overflow: hidden; }
  body {
    position: relative;
    background: linear-gradient(to bottom, var(--bg-top), var(--bg-bottom));
    font-family: "Source Sans 3", "Myriad Pro", sans-serif;
    color: var(--ink);
  }
  .sheet {
    position: absolute;
    background: var(--paper);
    box-shadow: 0 2px 8px rgba(0,0,0,.35);
    overflow: hidden;
  }
  .watermark { position: absolute; }

  /* Brand lockup */
  .brand { position: absolute; text-align: center; }
  .brand-mark { display: block; margin: 0 auto; }
  .brand-name {
    display: block;
    font-weight: 600;
    color: var(--ink);
    letter-spacing: .5px;
  }
  .brand-slogan {
    display: inline-block;
    font-weight: 600;
    color: var(--ink-dark);
    background: var(--yellow);
    letter-spacing: .2px;
    padding: 1px 4px;
    line-height: 1.2;
  }

  .footer-band { position: absolute; left: 0; bottom: 0; width: 100%; height: 8px; }

  /* Letterhead */
  .letterhead { left: 36px; top: 32px; width: 489px; height: 689px; }
  .letterhead .brand { left: 45px; top: 28px; width: 90px; }
  .letterhead .brand-name { font-size: 19px; margin-top: 2px; line-height: 1; }
  .letterhead .brand-slogan { font-size: 8px; margin-top: 6px; }
  .letterhead .contact {
    position: absolute; left: 322px; top: 46px;
    font-size: 8.4px; line-height: 11.4px; color: var(--ink);
  }
  .letterhead .contact .company { font-weight: 600; }
  .salutation {
    position: absolute; left: 49px; top: 192px;
    font-size: 13.5px; color: var(--ink);
  }
  .body-copy {
    position: absolute; left: 49px; top: 234px; width: 394px;
    font-size: 7.4px; line-height: 11.7px; text-align: justify; color: var(--ink);
  }
  .body-copy p { margin-bottom: 11.7px; }
  .signoff { position: absolute; left: 49px; top: 479px; font-size: 7.6px; color: var(--ink); }
  .signature {
    position: absolute; left: 48px; top: 496px; width: 63px; height: 28px;
    background: linear-gradient(90deg, rgba(40,40,60,.08), rgba(40,40,60,.02));
  }
  .signer { position: absolute; left: 48px; top: 537px; color: var(--ink); }
  .signer-name { font-size: 8.8px; text-transform: uppercase; display: block; line-height: 1.1; }
  .signer-title { font-size: 6.8px; display: block; }

  /* Envelope back */
  .envelope-back { left: 615px; top: 332px; width: 548px; height: 248px; }
  .envelope-back .flap { position: absolute; left: 0; top: 0; }
  .envelope-back .brand { left: 209px; top: 21px; width: 130px; }
  .envelope-back .brand-name { font-size: 8px; margin-top: 1px; }
  .envelope-back .brand-slogan {
    font-size: 8.8px; margin-top: 2px;
    background: var(--ink-dark); color: var(--yellow);
  }

  /* Envelope front */
  .envelope-front { left: 547px; top: 470px; width: 550px; height: 251px; }
  .envelope-front .brand { left: 22px; top: 22px; width: 80px; }
  .envelope-front .brand-name { font-size: 16px; margin-top: 2px; line-height: 1; }
  .envelope-front .brand-slogan { font-size: 7.4px; margin-top: 4px; }
  .envelope-front .contact {
    position: absolute; left: 27px; top: 117px;
    font-size: 8.8px; line-height: 11.8px; color: var(--ink);
  }
</style>
</head>
<body>

  <section class="sheet letterhead">
    <svg class="watermark" style="left:68px;top:174px" width="356" height="356" viewBox="0 0 356 356" aria-hidden="true">
      <circle cx="178" cy="178" r="168" fill="none" stroke="var(--mark-faint)" stroke-width="18"/>
    </svg>

    <div class="brand">
      <svg class="brand-mark" width="48" height="48" viewBox="0 0 48 48" aria-hidden="true">
        <circle cx="24" cy="24" r="21" fill="none" stroke="var(--ink)" stroke-width="4"/>
      </svg>
      <span class="brand-name">KORVANEL</span>
      <span class="brand-slogan">MADE WITH PRIDE</span>
    </div>

    <div class="contact">
      <span class="company">Korvanel Valves Pte. Ltd. (Singapore)</span><br>
      Registration no: 201947162K<br>
      Tel: (65) 6218 4906<br>
      Fax: (65) 6241 7089<br>
      sales@korvanelvalves.example<br>
      www.korvanelvalves.example
    </div>

    <p class="salutation">Dear Mr. Hartley,</p>

    <div class="body-copy">
      <p>Lorem ipsum dolor sit amet, consectetur adipiscing elit. Donec orci purus, luctus vitae dignissim eu, iaculis sed purus. Vivamus faucibus, ipsum nec aliquet viverra, leo mauris condimentum ligula, sit amet sagittis enim ligula quis arcu. Nam egestas tortor id nisi porttitor mattis. In tortor ante, ultricies in suscipit a, tempus non massa. Vivamus et auctor mi. Fusce vel massa nulla. Phasellus nec eros mauris, et scelerisque orci.</p>
      <p>Donec malesuada orci vitae nulla accumsan porta a id massa. Quisque accumsan iaculis magna sit amet fringilla. Maecenas consequat, magna eget tincidunt semper, odio nibh rutrum mi, id feugiat ante nisi eu risus. Vestibulum nunc orci, rhoncus a placerat in, ultricies in mi. Cras mattis varius eros, vel fringilla nisi suscipit eget. Quisque scelerisque sagittis nulla at porttitor.</p>
      <p>Sed id augue vitae urna euismod commodo aliquet a quam. Pellentesque arcu velit, cursus et malesuada ut, consequat et diam. Nullam erat sem, rhoncus id ullamcorper vitae, rhoncus et arcu. In ultricies ultricies nulla, ut rutrum nisi iaculis at. Donec eu magna a metus ornare faucibus. Fusce aliquet faucibus ultricies. Morbi semper, est id tincidunt gravida, sem arcu adipiscing lacus, ac bibendum nulla leo eu purus. Quisque nec diam sed risus consectetur a accumsan quis quis nibh. Vestibulum id purus lorem.</p>
      <p>It is a long established fact that a reader will be distracted by the readable content of a page when looking at its layout. The point of using Lorem Ipsum is that it has a more-or-less normal distribution of letters, as opposed to using 'Content here, content here', making it look like readable English. Many desktop publishing packages</p>
    </div>

    <p class="signoff">Sincerely,</p>
    <div class="signature" role="img" aria-label="Handwritten signature of Daniel Hartley"></div>
    <div class="signer">
      <span class="signer-name">Daniel Hartley</span>
      <span class="signer-title">CEO/ Founder</span>
    </div>

    <svg class="footer-band" viewBox="0 0 489 8" preserveAspectRatio="none" aria-hidden="true">
      <polygon points="0,0 371,0 368,8 0,8" fill="var(--yellow)"/>
      <polygon points="373,0 489,0 489,8 370,8" fill="var(--band-grey)"/>
    </svg>
  </section>

  <section class="sheet envelope-back">
    <svg class="flap" width="548" height="92" viewBox="0 0 548 92" aria-hidden="true">
      <path d="M0,0 H548 L535,70 Q531,90 511,90 H37 Q17,90 13,70 Z" fill="var(--yellow)"/>
    </svg>
    <div class="brand">
      <svg class="brand-mark" width="36" height="36" viewBox="0 0 36 36" aria-hidden="true">
        <circle cx="18" cy="18" r="15.5" fill="none" stroke="var(--ink)" stroke-width="3"/>
      </svg>
      <span class="brand-name">KORVANEL</span>
      <span class="brand-slogan">MADE WITH PRIDE</span>
    </div>
  </section>

  <section class="sheet envelope-front">
    <svg class="watermark" style="left:308px;top:19px" width="214" height="214" viewBox="0 0 214 214" aria-hidden="true">
      <circle cx="107" cy="107" r="99" fill="none" stroke="var(--mark-faint)" stroke-width="14"/>
    </svg>

    <div class="brand">
      <svg class="brand-mark" width="44" height="44" viewBox="0 0 44 44" aria-hidden="true">
        <circle cx="22" cy="22" r="19.5" fill="none" stroke="var(--ink)" stroke-width="3.5"/>
      </svg>
      <span class="brand-name">KORVANEL</span>
      <span class="brand-slogan">MADE WITH PRIDE</span>
    </div>

    <div class="contact">
      sales@korvanelvalves.example<br>
      www.korvanelvalves.example
    </div>

    <svg class="footer-band" viewBox="0 0 550 8" preserveAspectRatio="none" aria-hidden="true">
      <polygon points="0,0 419,0 416,8 0,8" fill="var(--yellow)"/>
      <polygon points="421,0 550,0 550,8 418,8" fill="var(--band-grey)"/>
    </svg>
  </section>

</body>
</html>
```